Green Logistics / Last Mile Delivery Firm needs cool one-page website

FYI - We do have a detailed brief in the uploaded files section below
COMPANY
We recently launched the company Quillby Logistics which is a pioneer in urban green logistics and provides zero-emissions last mile delivery services (i.e. delivery of parcels with delivery vans to the doorstep of households) for its logistics and retail clients.
We take on urban parcel delivery for our clients with a 100% electric commercial vehicles fleet, fair and sustainable working conditions for our employees and an unparalleled professional and customer-focused mindset.
WEBSITE
In the detailed brief, we have provided examples to emulate. We need the design + coding of the website. Website needs to be friendly/optimized for and should open swiftly on both Android & iOS.
In general, the website should convey
- green mission of the company
- sustainability (good working conditions, focus on employees)
- customer orientation
- professionalism
DESIGN
In the detailed brief, we have provided designs to emulate.
Color design: we do have a logo which features 2 green colors (one lighter and one darker color tone). However, the colors on the website do not necessarily need to follow these 2 colors exactly as we are able to switch the logo colors.
Imagery: should reflect maybe 50% green/leaf/tree , 25% customer and employee orientation, and 25% logistics (here it's important that it is the last mile delivery, i.e. delivery with delivery vans to the doorstep of households)

```html
<!DOCTYPE html>
<html lang="en">
<head>
<meta charset="utf-8">
<title>Quillby Logistics – Sustainable Last Mile</title>
<link href="https://fonts.googleapis.com/css2?family=Oswald:wght@400;500;600&family=Lato:wght@400;700&display=swap" rel="stylesheet">
<style>
:root{
  --green-dark:#1f9a3d;
  --green-mid:#2aa946;
  --green-light:#8cc63f;
  --lime:#a6d33a;
  --ink:#2b2b2b;
  --muted:#666;
  --line:#d9d9d9;
  --card:#f1f1f1;
  --footer:#262626;
  --red:#d8252a;
  --white:#fff;
}
*{box-sizing:border-box;margin:0;padding:0}
html,body{width:1200px;height:5141px;overflow:hidden}
body{position:relative;font-family:'Lato',sans-serif;color:var(--ink);background:var(--white);font-size:11px;line-height:1.55}
.abs{position:absolute}
h1,h2,h3,h4{font-family:'Oswald',sans-serif;font-weight:500;text-transform:uppercase;letter-spacing:.2px}
.btn-outline{position:absolute;border:2px solid var(--lime);color:var(--lime);border-radius:22px;font-size:10px;text-transform:uppercase;display:flex;align-items:center;justify-content:center;letter-spacing:.5px}
.brand{display:flex;align-items:center;gap:8px;font-family:'Oswald',sans-serif;font-weight:600;color:var(--lime);text-transform:uppercase}
.brand .dot{width:34px;height:34px;border-radius:50%;background:var(--green-dark)}
.section-title{position:absolute;left:0;width:1200px;text-align:center;font-size:30px;color:var(--ink)}
.title-mark{position:absolute;left:591px;width:18px;height:18px;border-radius:50%;background:var(--green-light)}

/* hero */
.hero{position:absolute;left:0;top:0;width:1200px;height:830px;background:linear-gradient(180deg,#3b5236 0%,#5d6d55 30%,#6b6f66 60%,#4e504b 100%)}
.topbar{position:absolute;left:0;top:0;width:1200px;height:40px;background:rgba(20,60,20,.45);color:#fff;font-size:10px}
.topbar span{position:absolute;top:12px;display:flex;align-items:center;gap:8px}
.nav{position:absolute;top:78px;left:432px;display:flex;gap:22px;color:#fff;font-size:11px;font-weight:700;text-transform:uppercase}
.hero-title{position:absolute;top:370px;left:0;width:1200px;text-align:center;color:#fff;font-size:32px}
.hero-sub{position:absolute;top:418px;left:0;width:1200px;text-align:center;color:#fff;font-size:20px}
.arrow{position:absolute;top:395px;width:20px;height:20px}
.dots{position:absolute;top:675px;left:571px;display:flex;gap:5px}
.dots i{width:6px;height:6px;border-radius:50%;background:rgba(255,255,255,.45)}
.dots i.on{background:var(--lime)}

/* about */
.about{position:absolute;left:112px;top:904px;width:966px;height:296px;border:2px solid var(--line);display:flex}
.about .col{flex:1;padding:28px 30px 0 36px;border-right:1px solid var(--line);margin:20px 0}
.about .col:last-child{border-right:0}
.about .col{padding-top:8px}
.col-head{display:flex;align-items:center;gap:12px;margin-bottom:20px}
.col-head h3{font-size:19px}
.col p{font-size:10.2px;color:var(--muted);margin-bottom:12px;line-height:1.6}

/* comparison */
.band-left{position:absolute;left:0;top:1362px;width:536px;height:413px;background:var(--green-dark)}
.band-right{position:absolute;left:666px;top:1362px;width:534px;height:413px;background:var(--green-light)}
.compare-card{position:absolute;top:1392px;width:540px;height:290px;background:#fff;box-shadow:0 4px 18px rgba(0,0,0,.12)}
.compare-card h3{position:absolute;top:46px;font-size:19px}
.compare-card ul{position:absolute;top:94px;list-style:none}
.compare-card li{display:flex;align-items:flex-start;gap:14px;font-size:13px;margin-bottom:20px}
.compare-card.no li{text-decoration:line-through}
.center-mark{position:absolute;left:506px;top:1468px;width:188px;height:188px;border-radius:50%;background:var(--green-mid)}

/* services */
.service{position:absolute;top:1970px;width:216px;height:216px;background:var(--card);text-align:center;border-radius:4px}
.service svg{position:absolute;left:50%;top:30px;transform:translateX(-50%)}
.service h4{position:absolute;top:96px;left:0;width:100%;font-size:13px;font-weight:500}
.service p{position:absolute;top:132px;left:30px;width:156px;font-size:10.5px;color:var(--muted);line-height:1.7}

/* contact band */
.cta{position:absolute;left:0;top:2284px;width:1200px;height:364px;background:radial-gradient(ellipse at 30% 40%,#2f6b3c 0%,#183f24 45%,#0d2616 100%)}
.cta h2{position:absolute;left:148px;top:130px;color:#fff;font-size:30px}
.cta p{position:absolute;left:148px;top:182px;width:680px;color:#fff;font-size:10px;line-height:1.45}

/* careers */
.careers-intro{position:absolute;left:160px;top:2796px;width:880px;text-align:center;font-size:9.6px;color:var(--muted);line-height:1.8}
.jobs{position:absolute;left:150px;top:2956px;width:430px;list-style:none}
.jobs li{height:55px;border-bottom:1px solid var(--line);display:flex;align-items:center;gap:24px;font-size:12px;color:#333;padding-left:2px}
.jobs li:last-child{border-bottom:0}
.plus{color:var(--green-dark);font-size:18px;font-weight:700;width:10px}
.photo-frame{position:absolute;left:634px;top:2946px;width:430px;height:352px;background:var(--green-dark)}
.photo{position:absolute;left:610px;top:2964px;width:432px;height:314px;background:linear-gradient(120deg,#3d4650 0%,#7d8790 40%,#b5bcc2 70%,#5e6a5a 100%)}

.details{position:absolute;left:148px;top:3346px;width:904px;height:804px;border:1px solid var(--line);border-top:6px solid var(--green-light);padding:60px 58px}
.details h3{font-size:21px;margin-bottom:12px}
.details ul{list-style:none;margin-bottom:36px}
.details li{position:relative;padding-left:16px;font-size:12px;line-height:1.5;color:#444}
.details li:before{content:"";position:absolute;left:2px;top:7px;width:5px;height:5px;border-radius:50%;background:var(--green-dark)}
.details p{font-size:12px;color:#444;line-height:1.5}

/* contact */
.contact-lead{position:absolute;left:0;width:1200px;text-align:center;font-size:12px;color:#444}
.info{position:absolute;left:150px;display:flex;gap:18px}
.info h4{font-size:13px;font-weight:500}
.info p{font-size:12px;color:#444}
.field{position:absolute;border:1px solid #c9c9c9;border-radius:6px;font-size:11px;color:#aaa;padding:12px 22px}

/* footer */
.footer{position:absolute;left:0;top:4730px;width:1200px;height:411px;background:var(--footer);color:#fff}
.footer .brand{position:absolute;left:434px;top:80px;font-size:32px}
.footer .brand .dot{width:60px;height:60px}
.fnav{position:absolute;left:0;top:178px;width:1200px;display:flex;justify-content:center;gap:30px;font-size:13px;text-transform:uppercase}
.social{position:absolute;left:520px;top:242px;display:flex;gap:10px}
.social i{width:34px;height:34px;border-radius:50%;background:var(--lime);display:block}
.legal{position:absolute;top:318px;left:0;width:1200px;text-align:center;font-size:12px}
.fline{position:absolute;top:352px;left:0;width:1200px;height:1px;background:#4a4a4a}
.copy{position:absolute;top:376px;left:0;width:1200px;text-align:center;font-size:12px}
</style>
</head>
<body>

<!-- HERO -->
<section class="hero" role="img" aria-label="Photo of an electric delivery van driving along a green roadside">
  <div class="topbar">
    <span style="left:150px">
      <svg width="16" height="16" viewBox="0 0 24 24"><path fill="#a6d33a" d="M6.6 10.8a15 15 0 0 0 6.6 6.6l2.2-2.2c.3-.3.7-.4 1-.2 1.1.4 2.3.6 3.6.6.6 0 1 .4 1 1V20c0 .6-.4 1-1 1A17 17 0 0 1 3 4c0-.6.4-1 1-1h3.5c.6 0 1 .4 1 1 0 1.3.2 2.5.6 3.6.1.3 0 .7-.2 1z"/></svg>
      (+00) 00 555 0142 310
    </span>
    <span style="left:330px">
      <svg width="18" height="14" viewBox="0 0 24 18"><rect x="1" y="1" width="22" height="16" fill="#a6d33a"/><path d="M1 1l11 9 11-9" stroke="#2b5a2b" stroke-width="2" fill="none"/></svg>
      contact@quillbylogistics.com
    </span>
    <span style="left:986px">
      <i style="display:block;width:20px;height:12px;background:linear-gradient(180deg,#c33 0 50%,#fff 50%);"></i>EN
      <svg width="10" height="8" viewBox="0 0 10 8"><path d="M1 2l4 4 4-4" stroke="#fff" stroke-width="1.5" fill="none"/></svg>
    </span>
  </div>
  <div class="brand abs" style="left:150px;top:60px;font-size:18px"><span class="dot" style="width:56px;height:56px"></span>Quillby Logistics</div>
  <nav class="nav"><span>Home</span><span>About</span><span>Services</span><span>Careers</span><span>Contact</span></nav>
  <a class="btn-outline" style="left:908px;top:64px;width:140px;height:38px">Get started</a>

  <svg class="arrow" style="left:52px" viewBox="0 0 20 20"><path d="M13 2L5 10l8 8" stroke="#fff" stroke-width="2.5" fill="none"/></svg>
  <svg class="arrow" style="left:1122px" viewBox="0 0 20 20"><path d="M7 2l8 8-8 8" stroke="#fff" stroke-width="2.5" fill="none"/></svg>

  <h1 class="hero-title">Quillby Logistics – Sustainable Last Mile</h1>
  <h2 class="hero-sub">Because we care about trees!</h2>
  <a class="btn-outline" style="left:530px;top:476px;width:140px;height:38px;color:#fff">Get started</a>
  <div class="dots"><i></i><i class="on"></i><i></i><i></i><i></i><i></i></div>
</section>
<svg class="abs" style="left:0;top:730px" width="1200" height="110" viewBox="0 0 1200 110">
  <path d="M0 110 L0 90 Q600 -10 1200 80 L1200 110 Z" fill="#fff"/>
  <path d="M0 90 Q600 -10 1200 80 L1200 90 Q600 10 0 98 Z" fill="#1f9a3d"/>
</svg>

<!-- ABOUT -->
<section class="about">
  <div class="col">
    <div class="col-head"><span style="width:42px;height:42px;border-radius:50%;background:var(--green-mid);display:block"></span><h3>Who we are</h3></div>
    <p>Quillby Logistics is a pioneer in urban green logistics and provides zeroemissions last mile delivery services for its logistics and retail clients.</p>
    <p>We take on urban parcel delivery for our clients with a 100% electric commercial vehicles fleet, fair and sustainable working conditions for our employees and an unparalleled professional and customer-focused mindset.</p>
  </div>
  <div class="col">
    <div class="col-head">
      <svg width="44" height="42" viewBox="0 0 44 42"><circle cx="20" cy="22" r="17" fill="none" stroke="#1f9a3d" stroke-width="4"/><circle cx="20" cy="22" r="9" fill="none" stroke="#8cc63f" stroke-width="4"/><path d="M20 22L38 4" stroke="#1f9a3d" stroke-width="3"/><path d="M33 3h6v6" stroke="#1f9a3d" stroke-width="3" fill="none"/></svg>
      <h3>Our mission</h3></div>
    <p>To satisfy consumers' ever-rising desire to buy products online, the CO2 emissions from delivery traffic will increase by 32% in the top 100 cities globally until 2030.</p>
    <p>Our clients care about our planet the same way we do, which is why Quillby Logistics helps to make the planet a better place by running the most environmentally friendly urban last mile possible.</p>
  </div>
  <div class="col">
    <div class="col-head">
      <svg width="66" height="40" viewBox="0 0 66 40"><rect x="0" y="6" width="10" height="26" fill="#1f9a3d"/><rect x="56" y="6" width="10" height="26" fill="#8cc63f"/><path d="M12 10l14 0 8 6 8-6 12 0v18l-14 10-10-6-18-4z" fill="#2aa946"/></svg>
      <h3>Our values</h3></div>
    <p>We see ourselves as a professional services company who strongly cares about the environment, its clients and their customers, as well as its employees.</p>
    <p>We believe that delivering parcels with zero emissions and providing a unique customer experience through a highly professional attitude and a great team spirit are the cornerstones for Quillby Logistics to operate in today's world in a sustainable yet profitable way.</p>
  </div>
</section>

<!-- COMPARISON -->
<h2 class="section-title" style="top:1268px">Quillby Logistics is...</h2>
<span class="title-mark" style="top:1318px"></span>
<div class="band-left"></div>
<div class="band-right"></div>
<div class="compare-card no" style="left:40px">
  <h3 style="left:104px;text-decoration:line-through">An ordinary parcel delivery firm</h3>
  <ul style="left:102px">
    <li><svg width="14" height="14" viewBox="0 0 14 14"><path d="M2 2l10 10M12 2L2 12" stroke="#d8252a" stroke-width="3"/></svg>Polluting our cities</li>
    <li><svg width="14" height="14" viewBox="0 0 14 14"><path d="M2 2l10 10M12 2L2 12" stroke="#d8252a" stroke-width="3"/></svg>Always in a rush</li>
    <li><svg width="14" height="14" viewBox="0 0 14 14"><path d="M2 2l10 10M12 2L2 12" stroke="#d8252a" stroke-width="3"/></svg>Short-term oriented</li>
    <li><svg width="14" height="14" viewBox="0 0 14 14"><path d="M2 2l10 10M12 2L2 12" stroke="#d8252a" stroke-width="3"/></svg>Focusing on profit only</li>
    <li><svg width="14" height="14" viewBox="0 0 14 14"><path d="M2 2l10 10M12 2L2 12" stroke="#d8252a" stroke-width="3"/></svg>Yet another parcel delivery firm</li>
  </ul>
</div>
<div class="compare-card" style="left:622px">
  <h3 style="left:120px">A pioneering green last mile</h3>
  <ul style="left:120px;width:330px">
    <li><svg width="22" height="18" viewBox="0 0 22 18"><path d="M2 9l6 6L20 2" stroke="#8cc63f" stroke-width="3" fill="none"/></svg>Delivering parcels emissions-free</li>
    <li><svg width="22" height="18" viewBox="0 0 22 18"><path d="M2 9l6 6L20 2" stroke="#8cc63f" stroke-width="3" fill="none"/></svg>Putting customer experience first</li>
    <li style="margin-bottom:4px"><svg width="22" height="18" viewBox="0 0 22 18" style="flex:none"><path d="M2 9l6 6L20 2" stroke="#8cc63f" stroke-width="3" fill="none"/></svg><span style="font-size:12.5px;line-height:1.2">Focusing on the environment, customers and employees</span></li>
    <li><svg width="22" height="18" viewBox="0 0 22 18"><path d="M2 9l6 6L20 2" stroke="#8cc63f" stroke-width="3" fill="none"/></svg>Focusing on profit only</li>
    <li><svg width="22" height="18" viewBox="0 0 22 18"><path d="M2 9l6 6L20 2" stroke="#8cc63f" stroke-width="3" fill="none"/></svg>A professional services company</li>
  </ul>
</div>
<span class="center-mark"></span>

<!-- SERVICES -->
<h2 class="section-title" style="top:1864px">Our services</h2>
<span class="title-mark" style="top:1916px"></span>
<div class="service" style="left:148px">
  <svg width="90" height="40" viewBox="0 0 90 40"><rect x="2" y="12" width="14" height="16" fill="#1f9a3d"/><path d="M20 10h34l12 10v12H20z" fill="#8cc63f"/><circle cx="30" cy="32" r="5" fill="#1f9a3d"/><circle cx="56" cy="32" r="5" fill="#1f9a3d"/><circle cx="80" cy="20" r="8" fill="none" stroke="#8cc63f" stroke-width="3"/></svg>
  <h4>Zero-emission delivery</h4><p>We operate a 100% electric commercial vehicle fleet</p></div>
<div class="service" style="left:378px">
  <svg width="50" height="52" viewBox="0 0 50 52"><circle cx="25" cy="12" r="10" fill="#1f9a3d"/><path d="M4 50c0-14 10-24 21-24s21 10 21 24z" fill="#8cc63f"/><circle cx="25" cy="40" r="7" fill="none" stroke="#1f9a3d" stroke-width="3"/></svg>
  <h4>Highly trained delivery drivers</h4><p>We only employ permanently, train far above average, and live a great team spirit</p></div>
<div class="service" style="left:608px">
  <svg width="40" height="52" viewBox="0 0 40 52"><circle cx="20" cy="18" r="14" fill="none" stroke="#1f9a3d" stroke-width="4"/><circle cx="20" cy="18" r="6" fill="#8cc63f"/><path d="M10 30l-6 18 8-4 4 6 4-14M30 30l6 18-8-4-4 6-4-14" fill="#8cc63f"/></svg>
  <h4>Professional all around</h4><p>We honor our commitments and hold ourselves to the highest professional standards</p></div>
<div class="service" style="left:836px">
  <svg width="44" height="44" viewBox="0 0 44 44"><circle cx="20" cy="24" r="16" fill="none" stroke="#1f9a3d" stroke-width="4"/><circle cx="20" cy="24" r="8" fill="none" stroke="#8cc63f" stroke-width="4"/><path d="M20 24L38 6" stroke="#1f9a3d" stroke-width="3"/></svg>
  <h4>Unparalleled customer focus</h4><p>We live a customer-oriented mindset, always measuring ourselves against their experience</p></div>

<!-- CTA BAND -->
<section class="cta" role="img" aria-label="Background photo of dense dark green tropical leaves">
  <h2>Get in touch with Quillby Logistics</h2>
  <p>If you got excited, or have a question about our services, our approach, our jobs or just want to get in touch to chat about how green logistics can make the planet a little bit better, please get in touch!</p>
  <a class="btn-outline" style="left:910px;top:172px;width:140px;height:38px">Contact us</a>
</section>

<!-- CAREERS -->
<h2 class="section-title" style="top:2690px">Careers</h2>
<span class="title-mark" style="top:2742px"></span>
<p class="careers-intro">If you join Quillby Logistics, you join a family. We elevate one another, care for each other's wellbeing and growth, and celebrate our successes. We strongly believe growth is a team sport and that every member of the family fully contributes to the achievements of the company overall. At the heart of everything we do at Quillby Logistics is a relentless focus on our mission. That's why we aim to ensure our employees can follow their own passion at the workplace, be this working in a truly collaborative and caring team, putting a smile on a customer's face or making the world a better place. While we are helping our clients grow by delivering their parcels, we are also helping all our employees grow personally and professionally. We care about our employees' happiness and wellbeing which is why we provide additional benefits like supplementary health insurance. If you are excited about joining our Quillby Logistics family, please check out our open positions.</p>
<ul class="jobs">
  <li><span class="plus">+</span>Full-time driver (m) for Berlin</li>
  <li><span class="plus">+</span>Full-time parcel deliverer (f) for Berlin</li>
  <li><span class="plus">+</span>Full-time driver (d) for Berlin</li>
  <li><span class="plus">+</span>Full-time parcel deliverer (d) for Berlin</li>
  <li><span class="plus">+</span>Full-time driver (f) for Berlin</li>
  <li><span class="plus">+</span>Full-time parcel deliverer (m) for Berlin</li>
</ul>
<div class="photo-frame"></div>
<div class="photo" role="img" aria-label="Photo of a delivery driver seated at the wheel inside a van cab"></div>

<section class="details">
  <h3>Your tasks as a delivery driver:</h3>
  <ul>
    <li>Delivery of packages to end customers</li>
    <li>In the delivery center: preparation of the tour and loading of the delivery van with parcels</li>
    <li>Drive from the delivery center to the delivery area - you will be guided by a navigation system</li>
    <li>Delivery of the parcels to end customers in the delivery area - the navigation helps you here too</li>
    <li>Suggest ideas for improvement in the delivery process</li>
    <li>Take care of and charge the delivery van</li>
  </ul>
  <h3>Required knowledge and skills:</h3>
  <ul>
    <li>Enjoy driving and dealing with customers</li>
    <li>Reliability, willingness to learn, and flexibility</li>
    <li>Customer orientation, teamwork and motivation</li>
    <li>Class B driving license and driving experience</li>
    <li>Certificate of good conduct without entries</li>
  </ul>
  <h3>What you can expected from the Quillby Logistics family:</h3>
  <ul>
    <li>A team that sees itself as a family and is there for each other</li>
    <li>A company that focuses on the environment, customers and its employees</li>
    <li>Above-average, performance-based remuneration</li>
    <li>Additional benefits such as company health insurance</li>
    <li>The latest, comfortable, fully electric delivery vehicles</li>
    <li>Fixed core working hours</li>
    <li>5-day week from Monday to Saturday with an alternating day off</li>
    <li>Training with full salary</li>
    <li>Private use of the company telephone</li>
    <li>Regular training and further development</li>
    <li>Coaching and mentoring by more experienced colleagues</li>
  </ul>
  <p>We offer a secure and varied job in a rapidly growing company with opportunities for advancement.<br>Interested? Send us an email or give us a call. We would like to invite you to a trial day.</p>
</section>

<!-- CONTACT -->
<h2 class="section-title" style="top:4220px">Contact</h2>
<span class="title-mark" style="top:4272px"></span>
<p class="contact-lead" style="top:4306px">We'd love to hear from you!</p>
<p class="contact-lead" style="top:4342px;left:170px;width:860px">Whether you have a question about our services, our approach, our jobs or just want to get in touch to chat about how green logistics can make the planet a little bit better, our team is ready to answer your questions and enquiries.</p>

<div class="info" style="top:4412px">
  <svg width="22" height="28" viewBox="0 0 22 28"><path d="M11 1a10 10 0 0 0-10 10c0 8 10 16 10 16s10-8 10-16A10 10 0 0 0 11 1z" fill="#8cc63f"/><circle cx="11" cy="11" r="4" fill="#fff"/></svg>
  <div><h4>Location:</h4><p>218 Alder Lane Westbrook, OR 97015</p></div>
</div>
<div class="info" style="top:4488px">
  <svg width="26" height="20" viewBox="0 0 26 20"><rect x="1" y="1" width="24" height="18" fill="#1f9a3d"/><path d="M1 1l12 10 12-10" stroke="#fff" stroke-width="2" fill="none"/></svg>
  <div><h4>Email:</h4><p>contact@quillbylogistics.com</p></div>
</div>
<div class="info" style="top:4566px">
  <svg width="24" height="24" viewBox="0 0 24 24"><path fill="#1f9a3d" d="M6.6 10.8a15 15 0 0 0 6.6 6.6l2.2-2.2c.3-.3.7-.4 1-.2 1.1.4 2.3.6 3.6.6.6 0 1 .4 1 1V20c0 .6-.4 1-1 1A17 17 0 0 1 3 4c0-.6.4-1 1-1h3.5c.6 0 1 .4 1 1 0 1.3.2 2.5.6 3.6.1.3 0 .7-.2 1z"/></svg>
  <div><h4>Call:</h4><p>(+00) 00 555 0142 310</p></div>
</div>

<div class="field" style="left:500px;top:4394px;width:266px;height:42px">Full Name</div>
<div class="field" style="left:780px;top:4394px;width:266px;height:42px">Phone#</div>
<div class="field" style="left:500px;top:4450px;width:546px;height:42px">Email Address</div>
<div class="field" style="left:500px;top:4506px;width:546px;height:118px">Message</div>
<a class="btn-outline" style="left:712px;top:4662px;width:140px;height:38px">Send message</a>

<!-- FOOTER -->
<footer class="footer">
  <div class="brand"><span class="dot"></span>Quillby Logistics</div>
  <nav class="fnav"><span>Home</span><span>About</span><span>Services</span><span>Careers</span><span>Contact</span></nav>
  <div class="social"><i></i><i></i><i></i></div>
  <p class="legal">Privacy policy &nbsp;-&nbsp; Terms &amp; conditions</p>
  <div class="fline"></div>
  <p class="copy">Copyright © 2020 Quillby Logistics.All Rights Reserved.</p>
</footer>

</body>
</html>
```